Bag packaging design of sliced bread

The project is for design of line of sliced bread with different flavours. The brand of the bread will be "Valorina". The shape of the bread will be oval. The bread will be packed in a bag. I attach the layout of the bag. The bag will be closed with a plastic clip. I attach images of similar products. The idea is to have one main design and then each colour to be different type of bread like those in the images 2 and 5.

```html
<!DOCTYPE html>
<html lang="en">
<head>
<meta charset="utf-8">
<title>Valorina Sliced Bread Bag</title>
<link rel="stylesheet" href="https://fonts.googleapis.com/css2?family=Montserrat:wght@600;700&family=Kaushan+Script&family=Oswald:wght@300;400&display=swap">
<style>
  :root {
    --page: #ffffff;
    --purple-deep: #6a2bb8;
    --purple-main: #7b35cf;
    --purple-bright: #9b4df0;
    --purple-light: #b77cf5;
    --label-white: #ffffff;
    --label-line: #6a2bb8;
    --brand-red: #b01e3a;
    --header-white: #ffffff;
    --outline: #333333;
    --crust-light: #e3b07f;
    --crust-mid: #c98a52;
    --crust-dark: #a66a38;
  }
  html, body {
    margin: 0;
    padding: 0;
    width: 1194px;
    height: 1200px;
    overflow: hidden;
    background: var(--page);
  }
  .bag-flat {
    position: absolute;
    left: 337px;
    top: 40px;
    width: 520px;
    height: 1120px;
  }
  .bag-flat svg { display: block; }
  .brand-name {
    font-family: "Montserrat", sans-serif;
    font-weight: 700;
    fill: var(--brand-red);
  }
  .variety {
    font-family: "Oswald", sans-serif;
    font-weight: 300;
    fill: var(--purple-deep);
  }
  .claim-caps {
    font-family: "Montserrat", sans-serif;
    font-weight: 700;
    fill: #ffffff;
  }
  .claim-script {
    font-family: "Kaushan Script", cursive;
    fill: #ffffff;
  }
  .net-weight {
    font-family: "Oswald", sans-serif;
    font-weight: 400;
    fill: #ffffff;
  }
</style>
</head>
<body>
<div class="bag-flat">
  <svg width="520" height="1120" viewBox="0 0 520 1120" xmlns="http://www.w3.org/2000/svg">
    <defs>
      <linearGradient id="breadTone" x1="0" y1="0" x2="0" y2="1">
        <stop offset="0" stop-color="var(--crust-mid)"/>
        <stop offset="0.3" stop-color="var(--crust-light)"/>
        <stop offset="0.6" stop-color="var(--crust-mid)"/>
        <stop offset="1" stop-color="var(--crust-light)"/>
      </linearGradient>
      <linearGradient id="ribbonTone" x1="0" y1="0" x2="0" y2="1">
        <stop offset="0" stop-color="var(--purple-bright)"/>
        <stop offset="0.5" stop-color="var(--purple-main)"/>
        <stop offset="1" stop-color="var(--purple-bright)"/>
      </linearGradient>
      <linearGradient id="baseTone" x1="0" y1="0" x2="0" y2="1">
        <stop offset="0" stop-color="var(--purple-main)"/>
        <stop offset="1" stop-color="var(--purple-deep)"/>
      </linearGradient>
      <linearGradient id="labelTone" x1="0" y1="0" x2="0" y2="1">
        <stop offset="0" stop-color="#ffffff"/>
        <stop offset="1" stop-color="#f1ecf5"/>
      </linearGradient>
    </defs>

    <!-- Header strip with hanging holes -->
    <rect class="bag-header" x="0" y="0" width="520" height="88" fill="var(--header-white)" stroke="var(--outline)" stroke-width="1"/>
    <circle cx="91" cy="44" r="22" fill="none" stroke="var(--outline)" stroke-width="1.2"/>
    <circle cx="429" cy="44" r="22" fill="none" stroke="var(--outline)" stroke-width="1.2"/>

    <!-- Sliced bread visual area -->
    <rect class="bread-visual" role="img" aria-label="Photo of stacked bread slices seen through the bag"
          x="0" y="88" width="520" height="1032" fill="url(#breadTone)"/>

    <!-- Ribbon band -->
    <path class="ribbon-band" d="M0 328 L520 328 L520 548 L0 548 Z" fill="url(#ribbonTone)"/>
    <path d="M0 340 L520 340" stroke="var(--purple-light)" stroke-width="2" opacity="0.6"/>
    <path d="M0 536 L520 536" stroke="var(--purple-light)" stroke-width="2" opacity="0.6"/>

    <!-- Central label -->
    <path class="label-frame"
          d="M150 330 Q260 300 370 330 Q400 330 405 355 Q385 440 405 525 Q400 550 370 550 Q260 580 150 550 Q120 550 115 525 Q135 440 115 355 Q120 330 150 330 Z"
          fill="var(--purple-deep)"/>
    <path d="M156 342 Q260 314 364 342 Q388 342 392 362 Q374 440 392 518 Q388 538 364 538 Q260 566 156 538 Q132 538 128 518 Q146 440 128 362 Q132 342 156 342 Z"
          fill="url(#labelTone)" stroke="var(--label-line)" stroke-width="1.5"/>
    <circle cx="260" cy="397" r="24" fill="var(--brand-red)"/>
    <text class="brand-name" x="260" y="466" text-anchor="middle" font-size="40">Valorina</text>
    <text class="variety" x="260" y="500" text-anchor="middle" font-size="21">Cu mala de secard</text>

    <!-- Natural seal -->
    <circle class="natural-seal" cx="264" cy="706" r="50" fill="none" stroke="#ffffff" stroke-width="4"/>

    <!-- Lower purple sweep -->
    <path class="sweep-light" d="M0 842 Q300 830 520 650 L520 1120 L0 1120 Z" fill="var(--purple-bright)" opacity="0.85"/>
    <path class="sweep-main" d="M0 872 Q320 860 520 690 L520 1120 L0 1120 Z" fill="url(#baseTone)"/>

    <!-- Claims -->
    <text class="claim-caps" x="260" y="952" text-anchor="middle" font-size="28">OVEN BAKED</text>
    <text class="claim-script" x="260" y="1004" text-anchor="middle" font-size="48">Fresh Bread</text>
    <text class="claim-caps" x="260" y="1057" text-anchor="middle" font-size="28">SOFT &amp; SMOOTH</text>
    <text class="net-weight" x="260" y="1097" text-anchor="middle" font-size="16">NET WEIGHT 500G</text>

    <rect x="0.5" y="0.5" width="519" height="1119" fill="none" stroke="var(--outline)" stroke-width="1"/>
  </svg>
</div>
</body>
</html>
```